Business Card Design Project- Removalist

I would like to surprise my husband to be with a different type of wedding present. His brother (who he owned a removalist business with) suddenly passed away from cancer recently and he has changed his business name to 'RTB' (which stands for Raising Tom Bright; but the full name doesn't need to be on the business card as it is more of a personal business name). To celebrate the new business I would like to get him some business cards made.
I would like the business name to be listed as 'RTB' and somewhere on the card I would like 'Sydney wide removals and relocation services'. I would like it to be obvious from the front of the card that it is a removalist business card. If a truck or some other feature that makes it look like a removalist business card could added it would be appreciated.
I don't mind what colours are used, but I would like the colour blue to feature somewhere in the design. It can be bright and fun, which is how Tom was.
I will also need the company's email address and phone number listed
The email address is: rtbremovals@quillpost.example
The contact number is: 0417 282 934
I don't need a contact name listed on the card, but perhaps 'Owned and operated by the Pendleworth family' could be added near the contact details in small font.
Thank you very much for considering this project!
Kind regards,
Fiona
Updates
Could you please change the mobile contact number to 0417 282 934. This is the only contact phone number required on the card now.
Thank you!

```html
<!DOCTYPE html>
<html lang="en">
<head>
<meta charset="utf-8">
<title>RTB business card</title>
<link rel="stylesheet" href="https://fonts.googleapis.com/css2?family=Tinos&family=PT+Sans&display=swap">
<style>
  :root {
    --orange: #f7941d;
    --navy: #0d2b50;
    --white: #ffffff;
    --ink: #1a1a1a;
    --grey-text: #3a3a3a;
    --rule: #555b63;
    --border: #8a8a8a;
    --serif: "Tinos", "Times New Roman", serif;
    --sans: "PT Sans", Arial, sans-serif;
  }
  * { box-sizing: border-box; margin: 0; padding: 0; }
  html, body {
    width: 1200px; height: 2180px; overflow: hidden;
    background: var(--white);
  }
  .card {
    position: absolute;
    left: 112px;
    width: 976px;
    overflow: hidden;
  }
  /* Front */
  .card-front { top: 128px; height: 612px; background: var(--orange); }
  .card-front .diagonal { position: absolute; inset: 0; }
  .front-name {
    position: absolute; left: 32px; top: 92px;
    font-family: var(--serif); font-size: 124px; line-height: 1;
    color: var(--white); font-weight: 400;
  }
  .front-badge {
    position: absolute; left: 500px; top: 252px;
    width: 224px; height: 176px;
  }
  .badge-name {
    position: absolute; inset: 0;
    display: flex; align-items: center; justify-content: center;
    font-family: var(--sans); color: var(--white);
    font-size: 60px; font-weight: 400; letter-spacing: 2px;
  }
  .front-tagline {
    position: absolute; left: 328px; top: 470px; width: 640px;
    text-align: center;
    font-family: var(--sans); font-size: 42px; line-height: 1.1;
    color: var(--white);
  }
  /* Back */
  .card-back {
    top: 808px; height: 544px;
    background: var(--white);
    border: 2px solid var(--border);
  }
  .back-name {
    position: absolute; left: 22px; top: 26px;
    font-family: var(--serif); font-size: 108px; line-height: 1;
    color: var(--navy);
  }
  .back-rule {
    position: absolute; left: 20px; top: 138px;
    width: 440px; height: 3px; background: var(--rule);
  }
  .owners {
    position: absolute; left: 22px; top: 146px; width: 460px;
    font-family: var(--sans); font-size: 34px; line-height: 1.1;
    color: var(--grey-text);
  }
  .contact {
    position: absolute; left: 22px; top: 372px;
    font-family: var(--sans); font-size: 33px; line-height: 1.3;
    color: var(--grey-text);
  }
  .back-tagline {
    position: absolute; left: 556px; top: 100px; width: 410px;
    text-align: center;
    font-family: var(--sans); font-size: 40px; line-height: 1.12;
    color: var(--ink);
  }
  .back-badge {
    position: absolute; left: 670px; top: 258px;
    width: 292px; height: 196px;
  }
</style>
</head>
<body>
  <section class="card card-front">
    <svg class="diagonal" width="976" height="612" viewBox="0 0 976 612" aria-hidden="true">
      <polygon points="48,612 976,22 976,612" fill="var(--navy)"/>
    </svg>
    <h1 class="front-name">RTB</h1>
    <div class="front-badge">
      <svg width="224" height="176" viewBox="0 0 224 176" aria-hidden="true">
        <ellipse cx="112" cy="88" rx="109" ry="85" fill="var(--navy)" stroke="var(--white)" stroke-width="4"/>
      </svg>
      <span class="badge-name">RTB</span>
    </div>
    <p class="front-tagline">Sydney wide removals and relocation services</p>
  </section>

  <section class="card card-back">
    <h2 class="back-name">RTB</h2>
    <div class="back-rule"></div>
    <p class="owners">Owned and operated by the Pendleworth family</p>
    <p class="contact">Contact -<br>rtbremovals@quillpost.example<br>0417 282 934</p>
    <p class="back-tagline">Sydney wide removals and relocation services</p>
    <div class="back-badge">
      <svg width="292" height="196" viewBox="0 0 292 196" aria-hidden="true">
        <ellipse cx="146" cy="98" rx="142" ry="94" fill="var(--navy)" stroke="#2f4f73" stroke-width="4"/>
        <ellipse cx="146" cy="98" rx="132" ry="85" fill="none" stroke="var(--white)" stroke-width="2"/>
      </svg>
      <span class="badge-name" style="font-size:72px">RTB</span>
    </div>
  </section>
</body>
</html>
```